Data Center Operator in India wants a new web design

We need a new web design for a data center operator in the Pan Indian market called Veltrano Data Centers (VDC). We are intending to build and operate a network of 7 data center facilities in 7 cities. We would like to see designs that use our corporate colors as per attached file. The final design should communicate our main concepts and values such as: dynamism, high technology, strength, safety, trustable company, future.
Updates

Target Market(s)

Top management and high skilled professionals mostly within the IT sector, belonging to worldwide multinationals

Coding

Coded - Design and coding required

Number of Pages Required

5+ page

Font styles to use
Sans Serif

Requirements
Must have
• VDC new web must have at least:
- "Home" page
- "About Us" page
- "Services" page
- "Our Data Centers" page
- "Industries" page
- "Why VDC?" page
- "Contact Us" page
Nice to have
• We want to have drop-down tabs for each of the main pages: About Us; Services; Our Data Centers; Industries; Why VDC?; Contact Us.
Search Bar & Social Media Buttons integrated on page.
Link to social media: Facebook, Linkedin, Instagram & Twitter.
Should not have
• No traditional Indian photos such as monuments, dancers, yogis or so

```html
<!DOCTYPE html>
<html lang="en">
<head>
<meta charset="utf-8">
<title>Veltrano Data Centers</title>
<link href="https://fonts.googleapis.com/css2?family=Exo+2:wght@400;500;600&family=Open+Sans:wght@400;600&display=swap" rel="stylesheet">
<style>
:root{
  --maroon:#6e1420;
  --ink:#222;
  --text:#555;
  --muted:#888;
  --line:#e2e2e2;
  --white:#fff;
  --footer:#1d1d1f;
  --footer-bar:#111;
  --grey-tile:#6f6f6f;
}
*{box-sizing:border-box;margin:0;padding:0}
html,body{width:1200px;height:4852px;overflow:hidden}
body{font-family:"Open Sans",sans-serif;color:var(--text);background:var(--white);position:relative;font-size:13px;line-height:1.6}
h1,h2,h3,h4{font-family:"Exo 2",sans-serif;font-weight:500;color:var(--ink)}
.abs{position:absolute}
.btn{display:inline-block;font-size:11px;padding:8px 20px;border:1px solid #bbb;color:var(--ink);background:var(--white)}
.btn-dark{background:var(--maroon);color:#fff;border-color:var(--maroon)}

.topbar{left:0;top:0;width:1200px;height:52px;background:var(--white);border-bottom:1px solid var(--line)}
.social{left:148px;top:14px;display:flex;gap:8px}
.social span{width:22px;height:22px;border:1px solid #555;border-radius:50%}
.brand{left:520px;top:10px;display:flex;align-items:center;gap:8px;font-family:"Exo 2",sans-serif;font-weight:600;color:var(--maroon);font-size:14px;line-height:1.1;width:200px}
.brand i{width:22px;height:22px;background:var(--maroon);flex:none}
.search{left:888px;top:15px;width:160px;height:22px;border:1px solid #ccc;font-size:10px;color:var(--muted);padding:2px 8px}
.navbar{left:0;top:52px;width:1200px;height:34px;background:rgba(20,20,20,.85);z-index:2}
.nav{left:268px;top:0;display:flex;height:34px;align-items:center;gap:2px}
.nav a{color:#ddd;font-size:11px;padding:6px 12px;text-decoration:none}
.nav a.active{background:#666;color:#fff}

.hero{left:0;top:52px;width:1200px;height:808px;background:linear-gradient(180deg,#5a0f19 0%,#7a1a26 45%,#a8505a 75%,#e9e2e3 100%)}
.hero-title{left:152px;top:318px;color:#fff}
.hero-title p{font-family:"Exo 2",sans-serif;font-size:22px;color:#fff;line-height:1.2}
.hero-title h1{font-size:50px;color:#fff;line-height:1.05}
.hero-copy{left:152px;top:428px;width:560px;color:#f3dfe1;font-size:11px}

.about{left:152px;top:688px;width:896px;height:584px;background:var(--white);box-shadow:0 6px 30px rgba(0,0,0,.15);text-align:center;padding:96px 120px 0}
.about h2{font-size:56px;line-height:1.1}
.about h2 b,.dc h2 b{color:var(--maroon);font-weight:500}
.about p{font-size:11px;margin-top:14px}
.about .btn{margin-top:52px}

.services{left:0;top:1300px;width:1200px;height:700px;background:radial-gradient(ellipse at 90% 40%,#ececec,transparent 55%)}
.services h2{position:absolute;top:96px;width:1200px;text-align:center;font-size:56px;line-height:1.2}
.services .lead{position:absolute;left:370px;top:190px;width:460px;text-align:center;font-size:11px}
.tiles{position:absolute;left:248px;top:312px;display:flex;gap:76px}
.tile{width:184px;height:180px;border-radius:14px;background:var(--white);box-shadow:0 4px 18px rgba(0,0,0,.15);display:flex;flex-direction:column;align-items:center;justify-content:center;font-size:13px;text-align:center;line-height:1.3;color:var(--text)}
.tile svg{margin-bottom:10px}
.tile.on{background:var(--grey-tile);color:#fff}
.services .btn{position:absolute;left:552px;top:562px}

.dc{left:0;top:2100px;width:1200px;height:640px}
.dc-map{left:560px;top:120px;width:600px;height:480px;background:radial-gradient(ellipse,#eeeeee,transparent 70%)}
.dc h2{position:absolute;left:152px;top:58px;font-size:56px;line-height:1.2}
.dc .copy{position:absolute;left:152px;top:148px;width:420px;font-size:11px}
.dc .copy p+p{margin-top:16px}
.dc .b1{position:absolute;left:152px;top:460px}
.dc .b2{position:absolute;left:152px;top:504px}
.locations{left:692px;top:188px;width:288px;height:352px;background:var(--white);box-shadow:0 4px 22px rgba(0,0,0,.15);padding:44px 32px}
.locations h3{text-align:center;font-size:22px;border-bottom:1px solid var(--line);padding-bottom:18px}
.locations ul{list-style:none;display:grid;grid-template-columns:1fr 1fr;row-gap:26px;margin-top:32px;font-size:11px}

.industries{left:0;top:2816px;width:1200px;height:584px;background:linear-gradient(180deg,#4e4e50,#8a8a8c 60%,#9a9a9c)}
.industries h2{position:absolute;top:104px;width:1200px;text-align:center;font-size:56px;line-height:1.2;color:#fff}
.ind-list{position:absolute;left:200px;top:246px;display:flex}
.ind{width:200px;text-align:center;color:#fff;font-size:12px;line-height:1.3}
.ind svg{display:block;margin:0 auto 10px}
.circle-arrow{width:44px;height:44px;border-radius:50%;background:#fff;display:flex;align-items:center;justify-content:center}
.industries .btn{position:absolute;left:552px;top:432px}

.why h2{position:absolute;top:3516px;width:1200px;text-align:center;font-size:56px;line-height:1.2}
.why-card{width:430px;height:240px;padding:36px}
.why-card.lift{background:var(--white);box-shadow:0 4px 22px rgba(0,0,0,.15)}
.why-card h3{font-size:22px;line-height:1.2}
.why-card p{font-size:11px;margin-top:14px}
.more-arrow{margin-top:16px}

.footer{left:0;top:4312px;width:1200px;height:500px;background:var(--footer);color:#bbb}
.footer h4{color:#fff;font-size:16px;margin-bottom:40px}
.footer ul{list-style:none;font-size:11px;line-height:2}
.fcol{position:absolute;top:76px}
.fsocial{display:flex;gap:6px;margin-top:14px}
.fsocial span{width:20px;height:20px;border-radius:50%;background:#3a6fa8}
.subscribe{display:flex;margin-top:20px}
.subscribe div{width:280px;height:34px;border:1px solid #666;font-size:11px;padding:8px 10px;color:#999}
.subscribe span{width:64px;height:34px;background:var(--maroon);color:#fff;font-size:11px;text-align:center;line-height:34px}
.bottombar{left:0;top:4812px;width:1200px;height:40px;background:var(--footer-bar);color:#aaa;font-size:10px;padding:12px 152px}
.call{left:1008px;top:4784px;width:40px;height:40px;border-radius:50%;background:#fff;display:flex;align-items:center;justify-content:center}
</style>
</head>
<body>

<header>
  <div class="abs topbar">
    <div class="abs social"><span></span><span></span><span></span><span></span></div>
    <div class="abs brand"><i></i>Veltrano Data Centers</div>
    <div class="abs search">Search</div>
  </div>
  <nav class="abs navbar">
    <div class="abs nav">
      <a class="active">Home</a><a>About Us ▾</a><a>Services ▾</a><a>Our Data Centers ▾</a><a>Industries ▾</a><a>Why VDC? ▾</a><a>Contact Us</a>
    </div>
  </nav>
</header>

<section class="abs hero" role="img" aria-label="Server room corridor with racks under deep red lighting"></section>
<div class="abs hero-title">
  <p>The World Best</p>
  <h1>Data Center Operator</h1>
</div>
<p class="abs hero-copy">Our facilities are built to keep critical systems online around the clock, with power, cooling and connectivity designed for growth. We help global teams scale with confidence and deliver services without pause to every user.</p>

<section class="abs about">
  <h2>About <b>Us</b></h2>
  <p>Veltrano Data Centers offer wholesale colocation services focused on the Indian market. Our facilities provide certified, reliable space for enterprises, supporting current demand and the fast growth driven by cloud computing, artificial intelligence, the Internet of Things, e-commerce, big data and virtual reality.</p>
  <p>We offer physical infrastructure and space, delivering reliability, security, modularity and scale, deployed significantly faster and more economically, and designed to meet immediate needs while delivering easy scalability.</p>
  <span class="btn btn-dark">Read More</span>
</section>

<section class="abs services">
  <h2>Our Services</h2>
  <p class="lead">We design, build and run secure spaces for critical IT loads, with flexible terms and expert support so your team can focus on growth, not on the hardware behind it.</p>
  <div class="tiles">
    <div class="tile">
      <svg width="52" height="52" viewBox="0 0 52 52" fill="none" stroke="#8a1d2a" stroke-width="2"><rect x="14" y="8" width="24" height="36" rx="2"/><line x1="18" y1="16" x2="34" y2="16"/><line x1="18" y1="24" x2="34" y2="24"/><line x1="18" y1="32" x2="34" y2="32"/></svg>
      Colocation<br>Services
    </div>
    <div class="tile on">
      <svg width="52" height="52" viewBox="0 0 52 52" fill="none" stroke="#fff" stroke-width="2"><circle cx="26" cy="26" r="6"/><circle cx="10" cy="12" r="4"/><circle cx="42" cy="12" r="4"/><circle cx="26" cy="44" r="4"/><path d="M13 15l8 7M39 15l-8 7M26 32v8"/></svg>
      Connectivity<br>Services
    </div>
    <div class="tile">
      <svg width="52" height="52" viewBox="0 0 52 52" fill="none" stroke="#8a1d2a" stroke-width="2"><circle cx="26" cy="26" r="9"/><path d="M26 8v6M26 38v6M8 26h6M38 26h6M13 13l4 4M35 35l4 4M39 13l-4 4M17 35l-4 4"/></svg>
      Support<br>Services
    </div>
  </div>
  <span class="btn">Read More</span>
</section>

<section class="abs dc">
  <div class="abs dc-map" role="img" aria-label="Faint dotted map of India marking data center cities"></div>
  <h2>Our Data <b>Centers</b></h2>
  <div class="copy">
    <p>Our network spans major Indian cities, placing capacity close to users and partners. Each site is engineered for uptime, with redundant power, cooling and carrier access. Sites follow one design standard, so customers can expand from one city to another with the same service, the same tools and the same trusted team.</p>
    <p>Every facility is staffed day and night by skilled engineers, with layered physical security and continuous monitoring that keeps your equipment safe.</p>
  </div>
  <span class="btn btn-dark b1">Technical Specifications</span>
  <span class="btn b2">Data Center Designs</span>
  <div class="abs locations">
    <h3>Locations</h3>
    <ul><li>Mumbai</li><li>NCR</li><li>Chennai</li><li>Ahmedabad</li><li>Hyderabad</li><li>Pune</li><li>Bangalore</li></ul>
  </div>
</section>

<section class="abs industries" role="img" aria-label="Grey-toned photograph of a modern office building">
  <h2>Industries</h2>
  <div class="abs circle-arrow" style="left:100px;top:254px"><svg width="14" height="14" viewBox="0 0 14 14"><path d="M9 2L4 7l5 5" stroke="#333" stroke-width="2" fill="none"/></svg></div>
  <div class="abs circle-arrow" style="left:1052px;top:254px"><svg width="14" height="14" viewBox="0 0 14 14"><path d="M5 2l5 5-5 5" stroke="#333" stroke-width="2" fill="none"/></svg></div>
  <div class="ind-list">
    <div class="ind"><svg width="46" height="46" viewBox="0 0 46 46" fill="none" stroke="#fff" stroke-width="2"><path d="M6 16L23 6l17 10zM10 18v18M18 18v18M28 18v18M36 18v18M6 38h34"/></svg>Government</div>
    <div class="ind"><svg width="46" height="46" viewBox="0 0 46 46" fill="none" stroke="#fff" stroke-width="2"><rect x="8" y="12" width="30" height="22"/><circle cx="23" cy="23" r="5"/></svg>Banking, Financial<br>Services &amp; Insurance</div>
    <div class="ind"><svg width="46" height="46" viewBox="0 0 46 46" fill="none" stroke="#fff" stroke-width="2"><path d="M6 10h6l5 20h18l4-14H14"/><circle cx="19" cy="36" r="2"/><circle cx="33" cy="36" r="2"/></svg>E-Commerce</div>
    <div class="ind"><svg width="46" height="46" viewBox="0 0 46 46" fill="none" stroke="#fff" stroke-width="2"><rect x="10" y="8" width="26" height="18" rx="2"/><path d="M23 26v8M12 38h22"/></svg>Managed &amp; Network<br>Service Providers</div>
  </div>
  <span class="btn">Read More</span>
</section>

<section class="why">
  <h2>Why VDC?</h2>
  <svg class="abs" style="left:60px;top:3916px" width="14" height="20" viewBox="0 0 14 20"><path d="M11 2L3 10l8 8" stroke="#555" stroke-width="2" fill="none"/></svg>
  <svg class="abs" style="left:1126px;top:3916px" width="14" height="20" viewBox="0 0 14 20"><path d="M3 2l8 8-8 8" stroke="#555" stroke-width="2" fill="none"/></svg>
  <div class="abs why-card lift" style="left:152px;top:3648px">
    <h3>PAN India Presence</h3>
    <p>Mumbai, Bangalore, Chennai, Hyderabad, NCR, Ahmedabad, Pune.<br>Built to sit directly in, or close to, major business hubs for low latency and smooth network reach.</p>
    <svg class="more-arrow" width="46" height="22" viewBox="0 0 46 22"><circle cx="11" cy="11" r="10" fill="none" stroke="#6e1420"/><path d="M6 11h36M37 6l5 5-5 5" stroke="#6e1420" fill="none"/></svg>
  </div>
  <div class="abs why-card" style="left:618px;top:3648px">
    <h3>Service Offerings</h3>
    <p>Wholesale Colocation<br>Caged and Dedicated Space<br>IT Managed Services</p>
    <svg class="more-arrow" width="46" height="22" viewBox="0 0 46 22"><circle cx="11" cy="11" r="10" fill="none" stroke="#6e1420"/><path d="M6 11h36M37 6l5 5-5 5" stroke="#6e1420" fill="none"/></svg>
  </div>
  <div class="abs why-card" style="left:152px;top:3940px">
    <h3>Tailor Made Solutions</h3>
    <p>Bespoke solutions tailored to the client's needs.<br>Secure and resilient solutions with scalable capacity.<br>Flexible terms, with contracted space including 24/7 NOC services.</p>
    <svg class="more-arrow" width="46" height="22" viewBox="0 0 46 22"><circle cx="11" cy="11" r="10" fill="none" stroke="#6e1420"/><path d="M6 11h36M37 6l5 5-5 5" stroke="#6e1420" fill="none"/></svg>
  </div>
  <div class="abs why-card" style="left:618px;top:3940px">
    <h3>Dedicated Power Delivery Infrastructure</h3>
    <p>Agreements in place with electricity distributors and renewable suppliers for uninterrupted power supply in every city we serve.</p>
    <svg class="more-arrow" width="46" height="22" viewBox="0 0 46 22"><circle cx="11" cy="11" r="10" fill="none" stroke="#6e1420"/><path d="M6 11h36M37 6l5 5-5 5" stroke="#6e1420" fill="none"/></svg>
  </div>
  <span class="abs btn btn-dark" style="left:548px;top:4266px">View More</span>
</section>

<footer class="abs footer">
  <div class="fcol" style="left:152px">
    <h4>Quick Links</h4>
    <ul><li>Home</li><li>About Us</li><li>Services</li><li>Our Data Centers</li><li>Industries</li><li>Why VDC?</li><li>Contact Us</li></ul>
  </div>
  <div class="fcol" style="left:432px">
    <h4>Others</h4>
    <ul><li>Location</li><li>Harbor Lane 27</li><li>Pune 411001</li><li>India</li></ul>
    <div class="fsocial"><span></span><span></span><span></span><span></span></div>
  </div>
  <div class="fcol" style="left:688px;width:360px">
    <h4>Newsletter Subscription</h4>
    <p style="font-size:11px">Sign up for news on new sites, capacity updates and events from our team across India.</p>
    <div class="subscribe"><div>Email Address</div><span>Send</span></div>
  </div>
</footer>
<div class="abs bottombar">Copyright Veltrano Data Center 2017 All Right Reserved</div>
<div class="abs call"><svg width="18" height="18" viewBox="0 0 24 24"><path d="M6.6 10.8a15 15 0 006.6 6.6l2.2-2.2a1 1 0 011-.25 11 11 0 003.6.6 1 1 0 011 1V20a1 1 0 01-1 1A17 17 0 013 4a1 1 0 011-1h3.5a1 1 0 011 1 11 11 0 00.6 3.6 1 1 0 01-.25 1z" fill="#222"/></svg></div>

</body>
</html>
```